Mobile Oil Change company needs a flyer to promote new business

We need a flyer to 1) print & handout and 2) email out to potential customers. We are a mobile oil change company that comes to our customer locations to perform the work instead of customers going to traditional oil change companies. We have a 21 point inspection with our oil change. (21 point inspection details will not be on the flyer). Would like to keep the flyer simple but creative. I'm attaching 1) the write-up we created, 2) our logo (logo color is dark teal on white but other combinations are included if you wanted to propose a different color combination), and 3) additional services we offer. Logo font is Alegreya Sans.
Would like the additional services listed with icons and brief descriptions (similar to attachment) without pricing. Company website for reference is www.brindlefleetcare.com.

Target Market(s)

Companies with many service vehicles such as Oil & Gas service companies, heating and air conditioning companies, utility companies, police departments, etc. Companies that prioritize convenience and maintenance first.

Font styles to use
Sans Serif

Colors
00a990

Requirements
Must have
• Simple but creative design with our logo at top of the flyer. Additional Services (details in document supplied) can be smaller and less prominent than other "main" content listed in the CONTENT document supplied.
Should not have
• Do not use animated character graphics in the flyer and limit (1) stock photos to A small area in the flyer.

```html
<!DOCTYPE html>
<html lang="en">
<head>
<meta charset="utf-8">
<title>Brindle Fleet Care – Mobile Oil Change Flyer</title>
<link href="https://fonts.googleapis.com/css2?family=Alegreya+Sans:wght@400;500;700;800&display=swap" rel="stylesheet">
<style>
  :root {
    --teal-dark: #134e4f;
    --teal-mid: #0f6a66;
    --teal-bright: #00a990;
    --ink: #1d1d1d;
    --paper: #ffffff;
    --mist: #e4e9e9;
    --backdrop: #3b3b3b;
  }
  * { margin: 0; padding: 0; box-sizing: border-box; }
  html, body { width: 1200px; height: 1200px; overflow: hidden; }
  body {
    background: var(--backdrop);
    font-family: "Alegreya Sans", sans-serif;
    color: var(--ink);
    position: relative;
  }
  .flyer {
    position: absolute; left: 240px; top: 95px;
    width: 720px; height: 1010px;
    background: var(--paper);
    overflow: hidden;
  }
  .abs { position: absolute; }

  /* header */
  .header { left: 0; top: 0; width: 720px; height: 320px; }
  .phone { left: 38px; top: 8px; color: #fff; font-size: 22px; font-weight: 400; }
  .brand {
    left: 0; width: 720px; top: 82px; text-align: center;
    color: #fff; font-size: 52px; font-weight: 800; letter-spacing: 1px;
  }
  .brand .mark {
    display: inline-block; width: 22px; height: 22px; background: #fff;
    border-radius: 50%; margin-right: 14px; vertical-align: middle;
  }
  .headline { left: 0; width: 720px; text-align: center; color: #fff; }
  .headline.main { top: 186px; font-size: 50px; font-weight: 700; letter-spacing: .5px; }
  .headline.sub { top: 250px; font-size: 40px; font-weight: 500; }

  /* process */
  .intro { left: 39px; top: 326px; width: 640px; font-size: 17.5px; line-height: 1.3; }
  .steps { left: 48px; top: 378px; list-style: none; }
  .step { position: absolute; left: 0; width: 560px; display: flex; align-items: center; font-size: 17.5px; white-space: nowrap; }
  .step-icon {
    width: 32px; height: 32px; background: var(--teal-dark); margin-right: 6px;
    display: flex; align-items: center; justify-content: center; flex: none;
  }
  .bottle-art {
    left: 504px; top: 354px; width: 200px; height: 192px;
    background: linear-gradient(160deg, #f3f5f5, #e7ecec);
    border-radius: 4px;
  }

  /* services */
  .rule { left: 0; width: 720px; height: 3px; background: var(--teal-bright); }
  .services-pill {
    left: 254px; top: 596px; width: 196px; height: 42px; border-radius: 21px;
    background: var(--teal-dark); color: #fff; font-size: 31px; font-weight: 500;
    text-align: center; line-height: 42px;
  }
  .service { width: 210px; text-align: center; }
  .service svg { display: block; margin: 0 auto 4px; }
  .service h3 { font-size: 12.5px; font-weight: 500; margin-bottom: 6px; }
  .service p { font-size: 9.5px; line-height: 1.3; }

  /* features */
  .features { left: 0; top: 874px; width: 720px; height: 65px; background: var(--mist); }
  .feature { position: absolute; top: 22px; display: flex; font-size: 13px; font-weight: 500; line-height: 1.1; }
  .feature svg { flex: none; margin: 4px 5px 0 0; }

  /* footer */
  .footer {
    left: 0; top: 950px; width: 720px; height: 60px; background: var(--teal-dark);
    color: #fff; font-size: 13px; display: flex; align-items: center; justify-content: center; gap: 28px;
  }
  .footer span { display: flex; align-items: center; gap: 7px; }
</style>
</head>
<body>
<main class="flyer">
  <svg class="abs header" viewBox="0 0 720 320" aria-hidden="true">
    <defs>
      <radialGradient id="headerGlow" cx="0.5" cy="0.05" r="0.75">
        <stop offset="0" stop-color="#00a990"/>
        <stop offset="0.55" stop-color="#0f6a66"/>
        <stop offset="1" stop-color="#134e4f"/>
      </radialGradient>
    </defs>
    <path d="M0 0H720V266Q430 330 0 286Z" fill="url(#headerGlow)"/>
  </svg>
  <div class="abs phone">Call&nbsp; - (833) 555-0142</div>
  <div class="abs brand"><span class="mark"></span>Brindle Fleet Care</div>
  <h1 class="abs headline main">HASSLE FREE</h1>
  <h2 class="abs headline sub">OIL CHANGES ON YOUR TERMS</h2>

  <p class="abs intro">Our simple 5-step process lets you schedule an appointment and get service to save time and money :</p>

  <ol class="abs steps">
    <li class="step" style="top:0">
      <span class="step-icon"><svg width="22" height="16" viewBox="0 0 22 16"><rect x="1" y="1" width="20" height="14" fill="#fff"/><path d="M1 1l10 8 10-8" stroke="#134e4f" stroke-width="1.4" fill="none"/></svg></span>1)&nbsp; Call or email us to schedule service</li>
    <li class="step" style="top:40px">
      <span class="step-icon" role="img" aria-label="Technician icon"><svg width="14" height="18"><rect x="1" y="1" width="12" height="16" rx="2" fill="#fff"/></svg></span>2)&nbsp; Our highly trained technicians come to you for service</li>
    <li class="step" style="top:85px">
      <span class="step-icon"><svg width="24" height="14" viewBox="0 0 24 14" fill="none" stroke="#fff" stroke-width="1.2"><rect x="5" y="1" width="11" height="9"/><path d="M16 4h4l3 3v3h-7"/><circle cx="9" cy="11.5" r="1.8"/><circle cx="19" cy="11.5" r="1.8"/><path d="M0 4h4M1 7h3"/></svg></span>3)&nbsp; Service is performed quickly on your vehicle</li>
    <li class="step" style="top:129px">
      <span class="step-icon"><svg width="16" height="20" viewBox="0 0 16 20" fill="none" stroke="#fff" stroke-width="1.2"><path d="M1 1h10l4 4v14H1z"/><path d="M4 9h8M4 12h8M4 15h6"/></svg></span>4)&nbsp; Pay agreed-upon pricing and receipt is emailed to you</li>
    <li class="step" style="top:173px">
      <span class="step-icon"><svg width="22" height="22" viewBox="0 0 22 22" fill="none" stroke="#fff" stroke-width="2"><circle cx="11" cy="11" r="6"/><circle cx="11" cy="11" r="2" fill="#fff"/><path d="M11 1v4M11 17v4M1 11h4M17 11h4"/></svg></span>5)&nbsp; Services performed are tracked electronically and reminders created</li>
  </ol>

  <div class="abs bottle-art" role="img" aria-label="Illustration of an oil bottle pouring into a funnel"></div>

  <div class="abs rule" style="top:608px"></div>
  <div class="abs rule" style="top:618px"></div>
  <h2 class="abs services-pill">Our Services</h2>

  <section class="abs service" style="left:23px;top:646px">
    <svg width="34" height="34" viewBox="0 0 34 34" fill="none" stroke="#00a990" stroke-width="1.5"><rect x="2" y="2" width="30" height="30"/><path d="M10 2v30M17 2v30M24 2v30M2 10h30M2 24h30"/></svg>
    <h3>Engine Air Filter Replacement</h3>
    <p>Maintain optimum engine performance.<br>Recommended every 15,000 - 30,000<br>miles.</p>
  </section>
  <section class="abs service" style="left:255px;top:646px">
    <svg width="34" height="34" viewBox="0 0 34 34" fill="none" stroke="#00a990" stroke-width="1.5"><rect x="6" y="2" width="22" height="30" rx="2"/><path d="M2 10q8-4 15 0t15 0M2 17q8-4 15 0t15 0M2 24q8-4 15 0t15 0"/></svg>
    <h3>Cabin Air Filter Replacement</h3>
    <p>Maintain a clean A/C and fan system.<br>Recommended every 12 months or<br>15,000 - 25,000</p>
  </section>
  <section class="abs service" style="left:487px;top:646px">
    <svg width="34" height="30" viewBox="0 0 34 30" fill="none" stroke="#00a990" stroke-width="1.5"><path d="M2 10q15-12 30 0L17 28z"/><path d="M17 28L24 6"/><path d="M10 4v-2M17 2v-2M24 4v-2" stroke-dasharray="2 2"/></svg>
    <h3>Wiperblade Replacement</h3>
    <p>Maintain excellent visibility on the road.<br>Recommended by 6-12 months.</p>
  </section>

  <section class="abs service" style="left:23px;top:764px">
    <svg width="36" height="36" viewBox="0 0 36 36" fill="none" stroke="#00a990" stroke-width="1.8"><circle cx="18" cy="18" r="16"/><circle cx="18" cy="18" r="11"/><circle cx="18" cy="18" r="3"/><path d="M7 16h8M21 16h8M18 21v8"/></svg>
    <h3>Power Steering Fluid Flush</h3>
    <p>Maintain proper power steering system health.<br>Recommended every 30,000 - 60,000 miles.</p>
  </section>
  <section class="abs service" style="left:255px;top:764px">
    <svg width="36" height="36" viewBox="0 0 36 36" fill="none" stroke="#00a990" stroke-width="1.5"><rect x="5" y="2" width="18" height="32" rx="2"/><rect x="9" y="6" width="10" height="8"/><path d="M23 10l6 4v14q0 3 3 0V16"/></svg>
    <h3>Fuel System Treatment</h3>
    <p>Clean your fuel system and injectors<br>to improve fuel economy.</p>
  </section>
  <section class="abs service" style="left:487px;top:764px">
    <svg width="36" height="36" viewBox="0 0 36 36" fill="none" stroke="#00a990" stroke-width="1.5"><circle cx="18" cy="18" r="16"/><circle cx="16" cy="20" r="10"/><circle cx="16" cy="20" r="3"/><path d="M26 6q6 4 6 12"/></svg>
    <h3>Brake Fluid Flush</h3>
    <p>Maintain an excellent functioning brake<br>system. Recommended every 2 years or<br>20,000 miles.</p>
  </section>

  <section class="abs features">
    <div class="feature" style="left:30px"><svg width="14" height="12" viewBox="0 0 14 12"><path d="M1 6l4 5L13 1" stroke="#134e4f" stroke-width="2.5" fill="none"/></svg><span>High quality synthetic oil used is best<br>suited for commercial vehicles</span></div>
    <div class="feature" style="left:261px"><svg width="14" height="12" viewBox="0 0 14 12"><path d="M1 6l4 5L13 1" stroke="#134e4f" stroke-width="2.5" fill="none"/></svg><span>Service includes a 21-point inspection</span></div>
    <div class="feature" style="left:489px"><svg width="14" height="12" viewBox="0 0 14 12"><path d="M1 6l4 5L13 1" stroke="#134e4f" stroke-width="2.5" fill="none"/></svg><span>Additional services are available</span></div>
  </section>

  <footer class="abs footer">
    <span><svg width="14" height="10" viewBox="0 0 14 10"><rect width="14" height="10" fill="#fff"/><path d="M0 0l7 6 7-6" stroke="#134e4f" fill="none"/></svg>Sales@BrindleFleetCare.com</span>
    <span>|</span>
    <span><svg width="14" height="14" viewBox="0 0 14 14" fill="none" stroke="#fff"><circle cx="7" cy="7" r="6"/><ellipse cx="7" cy="7" rx="2.6" ry="6"/><path d="M1 7h12"/></svg>www.brindlefleetcare.com</span>
  </footer>
</main>
</body>
</html>
```